Amber Hill House Brochure Design

We need a brochure designed for our Aged Care Facility. We need designs that portray warmth and welcoming and at the same time something professional. We have attached the previous brochure and are looking for a modern professional brochure. We are not set on sizing and welcome ideas.

Attachments:
- There are three files attached in this brief.
- One more high res photo is available via this link: https://www.filecrate.example/s/qm42tx7wpe0kdn3/House_High-Res_18.jpg?dl=0
- Another high res file has been added and is available through this link:
https://www.filecrate.example/s/vr83nc1yuf6jlo9/House_High-Res_24.jpg?dl=0

Target Market(s)

Aged Care and families

Requirements
Must have
• Logo and contact details

```html
<!DOCTYPE html>
<html lang="en">
<head>
<meta charset="utf-8">
<title>Amber Hill House – Trifold Brochure</title>
<link rel="stylesheet" href="https://fonts.googleapis.com/css2?family=Kalam:wght@400;700&family=Nunito:wght@400;600;700&display=swap">
<style>
  :root {
    --stage: #e6e8eb;
    --paper: #ffffff;
    --paper-grey: #f0f0f0;
    --blue: #1c8fd0;
    --blue-deep: #0d6eae;
    --blue-light: #5fb6e6;
    --navy: #1d4f78;
    --slate: #4f6f86;
    --ink: #1c1c1c;
    --quote-grey: #c9c9c9;
  }
  * { box-sizing: border-box; margin: 0; padding: 0; }
  html, body { width: 1200px; height: 800px; overflow: hidden; }
  body { background: var(--stage); position: relative; font-family: "Nunito", sans-serif; }

  .brochure {
    position: absolute; left: 60px; top: 120px;
    width: 1080px; height: 560px;
    display: flex;
    box-shadow: 0 18px 40px rgba(0,0,0,.18);
  }
  .panel { position: relative; width: 360px; height: 560px; overflow: hidden; }
  .panel-art { position: absolute; inset: 0; width: 100%; height: 100%; }
  .panel--intro { background: var(--paper); }
  .panel--contact { background: var(--paper-grey); }
  .panel--cover { background: var(--paper); }

  .script { font-family: "Kalam", cursive; }

  /* Intro panel */
  .intro-heading {
    position: absolute; left: 34px; top: 40px; width: 300px;
    font-family: "Kalam", cursive; font-size: 27px; line-height: 1.2;
    color: var(--blue-deep); font-weight: 400;
  }
  .intro-body {
    position: absolute; left: 44px; top: 188px; width: 290px;
    font-family: "Kalam", cursive; font-size: 24px; line-height: 1.25;
    color: var(--blue); font-weight: 700;
  }

  /* Contact panel */
  .quote-mark {
    position: absolute; left: 0; width: 100%; text-align: center;
    font-family: Georgia, serif; font-size: 70px; line-height: 1; color: var(--quote-grey);
  }
  .quote-mark--open { top: 24px; }
  .quote-mark--close { top: 196px; }
  .testimonial {
    position: absolute; left: 40px; top: 84px; width: 280px; text-align: center;
    font-family: "Kalam", cursive; font-size: 16px; line-height: 1.35; color: var(--blue-deep);
  }
  .testimonial-author { display: block; margin-top: 4px; color: var(--ink); font-size: 16px; }

  .brand {
    display: flex; align-items: center; gap: 8px;
    font-family: "Nunito", sans-serif; font-weight: 700; color: var(--slate);
    letter-spacing: .06em; text-transform: uppercase;
  }
  .brand-dot { border-radius: 50%; background: var(--slate); flex: none; }
  .brand--contact { position: absolute; left: 0; top: 272px; width: 100%; justify-content: center; font-size: 17px; }
  .brand--contact .brand-dot { width: 34px; height: 34px; }

  .contact-heading {
    position: absolute; left: 0; top: 322px; width: 100%; text-align: center;
    font-size: 20px; line-height: 1.2; font-weight: 600; color: var(--blue);
  }
  .contact-list { position: absolute; left: 70px; top: 384px; list-style: none; font-size: 14px; color: var(--ink); line-height: 1.3; }
  .contact-list li { display: flex; align-items: flex-start; gap: 8px; margin-bottom: 7px; }
  .contact-icon { width: 14px; height: 14px; flex: none; margin-top: 2px; fill: var(--navy); }
  .social { position: absolute; left: 0; top: 514px; width: 100%; display: flex; justify-content: center; gap: 10px; }
  .social-dot { width: 20px; height: 20px; border-radius: 50%; background: var(--navy); }

  /* Cover panel */
  .brand--cover { position: absolute; right: 20px; top: 20px; font-size: 11px; }
  .brand--cover .brand-dot { width: 24px; height: 24px; }
  .cover-heading {
    position: absolute; left: 26px; top: 44px; width: 200px;
    font-family: "Kalam", cursive; font-size: 17px; line-height: 1.25; color: var(--navy);
  }
  .cover-tagline {
    position: absolute; right: 26px; top: 420px; width: 280px; text-align: right;
    font-family: "Kalam", cursive; font-size: 18px; line-height: 1.25; color: #fff; font-weight: 700;
  }
  .web-pill {
    position: absolute; right: 22px; top: 508px; width: 290px; height: 26px;
    background: #fff; border-radius: 13px;
    display: flex; align-items: center; justify-content: center; gap: 6px;
    font-size: 12px; color: var(--ink);
  }
  .web-pill svg { width: 12px; height: 12px; fill: var(--navy); }
</style>
</head>
<body>
<main class="brochure">

  <!-- Inside flap -->
  <section class="panel panel--intro">
    <svg class="panel-art" viewBox="0 0 360 560" preserveAspectRatio="none" aria-hidden="true">
      <path d="M0 380 C120 350 240 360 360 330 L360 560 L0 560 Z" fill="var(--blue-deep)"/>
      <path d="M0 400 C120 372 240 382 360 356 L360 380 C240 404 120 396 0 424 Z" fill="#fff"/>
      <path d="M0 424 C120 396 240 404 360 380 L360 560 L0 560 Z" fill="var(--blue)"/>
    </svg>
    <svg class="panel-art" viewBox="0 0 360 560" role="img" aria-label="Photo: caring hands gently holding an elderly person's hand">
      <defs>
        <radialGradient id="handsTone" cx="50%" cy="45%" r="60%">
          <stop offset="0%" stop-color="#f3dccb"/>
          <stop offset="100%" stop-color="#d9b8a4"/>
        </radialGradient>
      </defs>
      <circle cx="185" cy="440" r="92" fill="#fff"/>
      <circle cx="185" cy="440" r="84" fill="url(#handsTone)"/>
    </svg>
    <h2 class="intro-heading">Amber Hill House Is An Accredited Government Funded Place.....</h2>
    <p class="intro-body">....aged care facility offering quality dignity and individuality for residents and their loved once.</p>
  </section>

  <!-- Back panel -->
  <section class="panel panel--contact">
    <div class="quote-mark quote-mark--open">&ldquo;</div>
    <blockquote class="testimonial">
      Since moving to Amber Hill House I have re-gained independence and are very appreciative of care provided by all staff.
      <cite class="testimonial-author">Margaret Ellison</cite>
    </blockquote>
    <div class="quote-mark quote-mark--close">&rdquo;</div>

    <div class="brand brand--contact"><span class="brand-dot"></span>Amber Hill House</div>

    <h3 class="contact-heading">Contact Us Today<br>For More Information</h3>
    <ul class="contact-list">
      <li>
        <svg class="contact-icon" viewBox="0 0 24 24"><path d="M12 2a7 7 0 0 0-7 7c0 5 7 13 7 13s7-8 7-13a7 7 0 0 0-7-7zm0 9.5A2.5 2.5 0 1 1 12 6.5a2.5 2.5 0 0 1 0 5z"/></svg>
        <span>48 Kestrel Way<br>Marlow Park QLD 4090</span>
      </li>
      <li>
        <svg class="contact-icon" viewBox="0 0 24 24"><path d="M6.6 10.8a15 15 0 0 0 6.6 6.6l2.2-2.2a1 1 0 0 1 1-.25 11.4 11.4 0 0 0 3.6.57 1 1 0 0 1 1 1V20a1 1 0 0 1-1 1A17 17 0 0 1 3 4a1 1 0 0 1 1-1h3.5a1 1 0 0 1 1 1c0 1.25.2 2.45.57 3.6a1 1 0 0 1-.25 1z"/></svg>
        <span>(07) 5550 1486</span>
      </li>
      <li>
        <svg class="contact-icon" viewBox="0 0 24 24"><path d="M6 2h12v5H6zM4 8h16a2 2 0 0 1 2 2v7h-4v5H6v-5H2v-7a2 2 0 0 1 2-2zm4 8v4h8v-4z"/></svg>
        <span>(07) 5550 1088</span>
      </li>
      <li>
        <svg class="contact-icon" viewBox="0 0 24 24"><path d="M12 2a10 10 0 1 0 0 20 10 10 0 0 0 0-20zm6.9 6h-3a15 15 0 0 0-1.3-3.9A8 8 0 0 1 18.9 8zM12 4c.8 1.2 1.5 2.5 1.9 4h-3.8c.4-1.5 1.1-2.8 1.9-4zM4.3 14a8 8 0 0 1 0-4h3.4a16 16 0 0 0 0 4zm.8 2h3a15 15 0 0 0 1.3 3.9A8 8 0 0 1 5.1 16zm3-8h-3a8 8 0 0 1 4.3-3.9A15 15 0 0 0 8.1 8zM12 20c-.8-1.2-1.5-2.5-1.9-4h3.8c-.4 1.5-1.1 2.8-1.9 4zm2.3-6H9.7a14 14 0 0 1 0-4h4.6a14 14 0 0 1 0 4zm.3 5.9a15 15 0 0 0 1.3-3.9h3a8 8 0 0 1-4.3 3.9zM16.3 14a16 16 0 0 0 0-4h3.4a8 8 0 0 1 0 4z"/></svg>
        <span>www.amberhillhouse.example</span>
      </li>
    </ul>
    <div class="social" aria-label="Social media links">
      <span class="social-dot"></span><span class="social-dot"></span><span class="social-dot"></span><span class="social-dot"></span>
    </div>
  </section>

  <!-- Front cover -->
  <section class="panel panel--cover">
    <svg class="panel-art" viewBox="0 0 360 560" preserveAspectRatio="none" aria-hidden="true">
      <path d="M0 150 C120 110 240 90 360 50 L360 80 C240 120 120 140 0 180 Z" fill="var(--blue)"/>
      <path d="M0 390 C120 380 240 330 360 270 L360 560 L0 560 Z" fill="var(--blue-deep)"/>
      <path d="M0 405 C120 392 240 350 360 292 L360 560 L0 560 Z" fill="var(--blue)"/>
    </svg>
    <svg class="panel-art" viewBox="0 0 360 560" preserveAspectRatio="none" role="img" aria-label="Photo: a smiling carer in a teal uniform helping an elderly resident seated at a table">
      <defs>
        <linearGradient id="careTone" x1="0" y1="0" x2="1" y2="1">
          <stop offset="0%" stop-color="#9fd3cc"/>
          <stop offset="55%" stop-color="#e8e2dc"/>
          <stop offset="100%" stop-color="#d99aa6"/>
        </linearGradient>
      </defs>
      <path d="M0 190 C120 150 240 130 360 90 L360 285 C240 345 120 382 0 384 Z" fill="url(#careTone)"/>
    </svg>
    <div class="brand brand--cover"><span class="brand-dot"></span>Amber Hill House</div>
    <h1 class="cover-heading">At Amber Hill House We're Committed To Your Care And Comfort</h1>
    <p class="cover-tagline">Providing<br>Aged Care With Quality,<br>Dignity And Individuality</p>
    <div class="web-pill">
      <svg viewBox="0 0 24 24"><circle cx="12" cy="12" r="10"/></svg>
      <span>www.amberhillhouse.example</span>
    </div>
  </section>

</main>
</body>
</html>
```